Dental Consulting Business Card - Stationary
Business Card / Stationary
Modern
Glen R. Castellano
President
4817 W. Harborview Ave.
Fort Lauderdale, FL
glen@zuvadentalconsulting.example
www.zuvadentalconsulting.example

```html
<!DOCTYPE html>
<html lang="en">
<head>
<meta charset="utf-8">
<title>ZuvaDental Business Card</title>
<link rel="stylesheet" href="https://fonts.googleapis.com/css2?family=Open+Sans:wght@400;600;700&display=swap">
<style>
:root{
  --page:#eceae6;
  --blue:#2b8fd3;
  --blue-dark:#1f78b6;
  --green:#8cc63f;
  --ink:#3b3f44;
  --muted:#6c7278;
  --white:#ffffff;
}
*{margin:0;padding:0;box-sizing:border-box}
html,body{width:1200px;height:629px;overflow:hidden}
body{background:var(--page);font-family:"Open Sans",Arial,sans-serif;position:relative}
.card{position:absolute;top:165px;width:520px;height:300px;border-radius:4px;overflow:hidden;box-shadow:0 6px 18px rgba(0,0,0,.18)}
.card--back{left:50px;background:var(--blue)}
.card--front{left:630px;background:var(--white)}
.brand{display:flex;align-items:center;gap:10px;font-weight:700;letter-spacing:-.5px}
.brand__dot{width:14px;height:14px;border-radius:50%}
.card--back .brand{position:absolute;left:0;right:0;top:112px;justify-content:center;color:var(--white);font-size:40px}
.card--back .brand__dot{background:var(--white)}
.tagline{position:absolute;left:0;right:0;bottom:38px;text-align:center;color:var(--white);font-size:13px;letter-spacing:.3px}
.card--front .brand{position:absolute;left:34px;top:104px;color:var(--ink);font-size:30px}
.card--front .brand__dot{background:var(--blue)}
.divider{position:absolute;left:258px;top:44px;width:1px;height:176px;background:#d4d7da}
.person{position:absolute;left:276px;top:44px}
.person__name{font-size:14px;font-weight:700;color:var(--blue)}
.person__title{font-size:11px;color:var(--muted)}
.contacts{position:absolute;left:276px;top:94px;list-style:none}
.contacts li{display:flex;align-items:flex-start;gap:8px;font-size:10.5px;line-height:13px;color:var(--ink);margin-bottom:6px}
.contacts svg{flex:none;width:13px;height:13px}
.footer-band{position:absolute;left:0;right:0;bottom:0;height:40px;background:var(--blue);border-top:5px solid var(--green)}
.footer-band__url{color:var(--white);font-size:12px;text-align:center;line-height:35px;letter-spacing:.4px}
</style>
</head>
<body>
<section class="card card--back" aria-label="Card back">
  <div class="brand"><span class="brand__dot"></span>ZuvaDental</div>
  <p class="tagline">Marketing | Media | Management</p>
</section>

<section class="card card--front" aria-label="Card front">
  <div class="brand"><span class="brand__dot"></span>ZuvaDental</div>
  <div class="divider"></div>
  <div class="person">
    <p class="person__name">Glen R. Castellano</p>
    <p class="person__title">President</p>
  </div>
  <ul class="contacts">
    <li><svg viewBox="0 0 14 14"><circle cx="7" cy="7" r="7" fill="#2b8fd3"/><path d="M7 3a2.4 2.4 0 0 0-2.4 2.4C4.6 7.2 7 10.5 7 10.5s2.4-3.3 2.4-5.1A2.4 2.4 0 0 0 7 3zm0 3.3a.9.9 0 1 1 0-1.8.9.9 0 0 1 0 1.8z" fill="#fff"/></svg><span>4817 W. Harborview Ave.<br>Fort Lauderdale, FL</span></li>
    <li><svg viewBox="0 0 14 14"><circle cx="7" cy="7" r="7" fill="#2b8fd3"/><path d="M5 3.5l1.2 1.8-.7.8c.4.9 1.1 1.6 2 2l.8-.7 1.8 1.2-.6 1.4C6.9 9.8 4.2 7.1 3.6 4.1z" fill="#fff"/></svg><span>T: 954.555.0147</span></li>
    <li><svg viewBox="0 0 14 14"><circle cx="7" cy="7" r="7" fill="#2b8fd3"/><rect x="3.5" y="4.5" width="7" height="5" fill="none" stroke="#fff" stroke-width="1"/><path d="M3.5 4.8L7 7.4l3.5-2.6" fill="none" stroke="#fff" stroke-width="1"/></svg><span>glen@zuvadentalconsulting.example</span></li>
    <li><svg viewBox="0 0 14 14"><circle cx="7" cy="7" r="7" fill="#2b8fd3"/></svg><span>morvanlq</span></li>
    <li><svg viewBox="0 0 14 14"><circle cx="7" cy="7" r="7" fill="#2b8fd3"/><circle cx="7" cy="7" r="3.6" fill="none" stroke="#fff" stroke-width="1"/><path d="M3.4 7h7.2M7 3.4c-1.6 2-1.6 5.2 0 7.2M7 3.4c1.6 2 1.6 5.2 0 7.2" fill="none" stroke="#fff" stroke-width=".8"/></svg><span>www.zuvadentalconsulting.example</span></li>
  </ul>
  <div class="footer-band"><p class="footer-band__url">www.zuvadentalconsulting.example</p></div>
</section>
</body>
</html>
```